Fire Hydrant Repair Parts Flyer

We need a flyer advertising both fire hydrant parts and the manufacturers that we are stocking. Our company is Coastal Flowline Supply and we are a parts distributor who sells directly to contractors. I have attached an example flyer that advertises some other parts we stock. We don't want it to look exactly like the old flyer, but we would like it to be structured similarly. I have also attached a background image for the flyer as well as some pictures of the parts we are stocking. I have also attached pictures of the manufacturer logos that we are stocking. We are trying to convey the parts that we are stocking which are: "Traffic Repair Kits", "Main Valve Repair Kits", "Extension Kits", "Replacement Caps & Gaskets", "Replacement Nozzles", Adjustable Hydrant Wrenches", "Hydrant Diffusers", & "Hydrant Oil". I have attached pictures of some of these items that we would like placed on the flyer. Let me know if you have any questions at all.

```html
<!DOCTYPE html>
<html lang="en">
<head>
<meta charset="utf-8">
<title>Fire Hydrant Repair Parts and Accessories</title>
<link rel="stylesheet" href="https://fonts.googleapis.com/css2?family=Montserrat:wght@700;800&family=Fira+Sans:wght@400;500;600;700&display=swap">
<style>
  :root {
    --blue: #3a4ea6;
    --red: #ec1f4f;
    --white: #ffffff;
    --panel: #e6e7e9;
    --ink: #2b2b2b;
    --stage: #2c2c2c;
  }
  * { box-sizing: border-box; margin: 0; padding: 0; }
  html, body { width: 948px; height: 1200px; overflow: hidden; background: var(--stage); }
  .flyer {
    position: absolute; left: 50px; top: 0; width: 848px; height: 1200px;
    background: var(--white); overflow: hidden;
    font-family: "Fira Sans", sans-serif;
  }
  .header-band { position: absolute; left: 0; top: 0; width: 848px; height: 518px; background: var(--blue); }
  .lower-panel { position: absolute; left: 0; top: 518px; width: 848px; height: 372px; background: var(--panel); }
  .feature-frame { position: absolute; left: 26px; top: 186px; width: 796px; height: 704px; background: var(--panel); }
  .title {
    position: absolute; left: 0; top: 34px; width: 848px; text-align: center;
    font-family: "Montserrat", sans-serif; font-weight: 800; font-size: 66px;
    letter-spacing: -1px; color: var(--white); line-height: 1; white-space: nowrap;
  }
  .subtitle {
    position: absolute; left: 30px; top: 103px; width: 792px; height: 63px;
    background: var(--red); border: 5px solid var(--white);
    font-family: "Montserrat", sans-serif; font-weight: 800; font-size: 48px;
    color: var(--white); text-align: center; line-height: 52px; letter-spacing: -0.5px;
    white-space: nowrap;
  }
  .hero-photo {
    position: absolute; left: 42px; top: 199px; width: 764px; height: 432px;
    background: linear-gradient(160deg, #7da84a 0%, #8c9aa6 35%, #b7bec4 55%, #e9eef0 75%, #6c9a3f 100%);
  }
  .stock-heading {
    position: absolute; left: 435px; top: 463px; width: 362px; height: 54px;
    background: var(--blue); color: var(--white); text-align: center;
    font-family: "Fira Sans", sans-serif; font-weight: 700; font-size: 38px; line-height: 54px;
    white-space: nowrap;
  }
  .stock-list {
    position: absolute; left: 435px; top: 530px; width: 360px; height: 357px;
    background: var(--red); list-style: none; padding: 22px 0 0 20px;
  }
  .stock-list li {
    display: flex; align-items: center; gap: 8px; height: 39.5px;
    color: var(--white); font-weight: 500; font-size: 19px; white-space: nowrap;
  }
  .stock-list svg { width: 15px; height: 15px; flex: none; }
  .parts-grid {
    position: absolute; left: 37px; top: 656px; width: 382px; height: 231px;
    display: grid; grid-template-columns: repeat(3, 1fr); grid-template-rows: repeat(2, 1fr);
  }
  .part-cell { border-right: 1px solid #c9cacc; border-bottom: 1px solid #c9cacc; padding: 8px; }
  .part-cell:nth-child(3n) { border-right: none; }
  .part-cell:nth-child(n+4) { border-bottom: none; }
  .part-photo { width: 100%; height: 100%; border-radius: 4px; background: radial-gradient(circle, #8e9095 0%, #cfd0d3 70%, var(--panel) 100%); }
  .part-photo.red { background: radial-gradient(circle, #c43040 0%, #c7c9cc 65%, var(--panel) 100%); }
  .part-photo.yellow { background: radial-gradient(circle, #e3b21f 0%, #cdcfd1 65%, var(--panel) 100%); }
  .part-photo.bottle { background: radial-gradient(ellipse 30% 50%, #f3f3f3 0%, #d3d4d6 70%, var(--panel) 100%); }
  .rule-blue { position: absolute; left: 0; top: 909px; width: 848px; height: 2px; background: var(--blue); }
  .brand-row {
    position: absolute; left: 36px; top: 925px; width: 780px; height: 70px;
    display: flex; align-items: center;
  }
  .brand {
    flex: 1; height: 100%; display: flex; align-items: center; justify-content: center; gap: 5px;
    border-right: 1px solid #333; font-weight: 600;
    font-size: 13px; color: var(--ink); text-align: center; line-height: 1.15; padding: 0 4px;
  }
  .brand:last-child { border-right: none; }
  .brand-dot { width: 14px; height: 14px; border-radius: 50%; background: var(--ink); flex: none; }
  .company {
    position: absolute; left: 0; top: 1030px; width: 848px;
    display: flex; justify-content: center; align-items: center; gap: 16px;
  }
  .company-square { width: 44px; height: 44px; background: var(--blue); }
  .company-name { font-weight: 500; font-size: 46px; color: var(--blue); white-space: nowrap; }
  .footer-call {
    position: absolute; left: 0; top: 1118px; width: 848px; height: 52px;
    background: linear-gradient(115deg, var(--red) 0 468px, var(--white) 468px 478px, var(--blue) 478px);
  }
  .call-label { position: absolute; left: 30px; top: 15px; font-weight: 600; font-size: 17px; color: var(--white); white-space: nowrap; }
  .call-number { position: absolute; left: 160px; top: 5px; font-weight: 700; font-size: 31px; color: var(--white); white-space: nowrap; }
  .call-web { position: absolute; left: 515px; top: 14px; font-weight: 500; font-size: 17px; letter-spacing: 3px; color: var(--white); white-space: nowrap; }
  .rule-red-thin { position: absolute; left: 0; top: 1172px; width: 848px; height: 3px; background: var(--red); }
  .rule-blue-thin { position: absolute; left: 0; top: 1179px; width: 848px; height: 2px; background: var(--blue); }
</style>
</head>
<body>
<main class="flyer">
  <div class="header-band"></div>
  <div class="lower-panel"></div>
  <div class="feature-frame"></div>

  <h1 class="title">FIRE HYDRANT REPAIR</h1>
  <h2 class="subtitle">PARTS AND ACCESSORIES</h2>

  <div class="hero-photo" role="img" aria-label="Photo of a red fire hydrant flushing a stream of water across a grassy roadside"></div>

  <div class="stock-heading">PARTS WE STOCK</div>
  <ul class="stock-list">
    <li><svg viewBox="0 0 16 16"><circle cx="8" cy="8" r="6.5" fill="none" stroke="#fff" stroke-width="1.4"/><path d="M5 8.2l2.2 2.2L13 3.5" fill="none" stroke="#fff" stroke-width="1.6"/></svg>Traffic Repair Kits</li>
    <li><svg viewBox="0 0 16 16"><circle cx="8" cy="8" r="6.5" fill="none" stroke="#fff" stroke-width="1.4"/><path d="M5 8.2l2.2 2.2L13 3.5" fill="none" stroke="#fff" stroke-width="1.6"/></svg>Main Valve Repair Kits</li>
    <li><svg viewBox="0 0 16 16"><circle cx="8" cy="8" r="6.5" fill="none" stroke="#fff" stroke-width="1.4"/><path d="M5 8.2l2.2 2.2L13 3.5" fill="none" stroke="#fff" stroke-width="1.6"/></svg>Extension Kits</li>
    <li><svg viewBox="0 0 16 16"><circle cx="8" cy="8" r="6.5" fill="none" stroke="#fff" stroke-width="1.4"/><path d="M5 8.2l2.2 2.2L13 3.5" fill="none" stroke="#fff" stroke-width="1.6"/></svg>Replacement Caps &amp; Gaskets</li>
    <li><svg viewBox="0 0 16 16"><circle cx="8" cy="8" r="6.5" fill="none" stroke="#fff" stroke-width="1.4"/><path d="M5 8.2l2.2 2.2L13 3.5" fill="none" stroke="#fff" stroke-width="1.6"/></svg>Replacement Nozzles</li>
    <li><svg viewBox="0 0 16 16"><circle cx="8" cy="8" r="6.5" fill="none" stroke="#fff" stroke-width="1.4"/><path d="M5 8.2l2.2 2.2L13 3.5" fill="none" stroke="#fff" stroke-width="1.6"/></svg>Adjustable Hydrant Wrenches</li>
    <li><svg viewBox="0 0 16 16"><circle cx="8" cy="8" r="6.5" fill="none" stroke="#fff" stroke-width="1.4"/><path d="M5 8.2l2.2 2.2L13 3.5" fill="none" stroke="#fff" stroke-width="1.6"/></svg>Hydrant Diffusers</li>
    <li><svg viewBox="0 0 16 16"><circle cx="8" cy="8" r="6.5" fill="none" stroke="#fff" stroke-width="1.4"/><path d="M5 8.2l2.2 2.2L13 3.5" fill="none" stroke="#fff" stroke-width="1.6"/></svg>Hydrant Oil</li>
  </ul>

  <div class="parts-grid">
    <div class="part-cell"><div class="part-photo" role="img" aria-label="Photo of a hydrant extension kit with gaskets and bolts"></div></div>
    <div class="part-cell"><div class="part-photo red" role="img" aria-label="Photo of a red replacement hydrant cap with chain"></div></div>
    <div class="part-cell"><div class="part-photo yellow" role="img" aria-label="Photo of a yellow hydrant diffuser with pressure gauge"></div></div>
    <div class="part-cell"><div class="part-photo bottle" role="img" aria-label="Photo of a bottle of hydrant oil"></div></div>
    <div class="part-cell"><div class="part-photo" role="img" aria-label="Photo of a traffic repair kit with coupling and bolts"></div></div>
    <div class="part-cell"><div class="part-photo" role="img" aria-label="Photo of an adjustable hydrant wrench"></div></div>
  </div>

  <div class="rule-blue"></div>
  <div class="brand-row">
    <div class="brand"><span class="brand-dot"></span>Northgate Flow Control</div>
    <div class="brand">Ridgeline Valve &amp; Hydrant</div>
    <div class="brand">Hartwell</div>
    <div class="brand">Brenmar Valve Co.</div>
    <div class="brand"><span class="brand-dot"></span>Kestrel Valve</div>
    <div class="brand">Lodestar Valve Company</div>
  </div>

  <div class="company">
    <span class="company-square"></span>
    <span class="company-name">Coastal Flowline Supply</span>
  </div>

  <div class="footer-call">
    <span class="call-label">Call Us Today !</span>
    <span class="call-number">(800) 555-0142</span>
    <span class="call-web">www.coastalflowline.com</span>
  </div>
  <div class="rule-red-thin"></div>
  <div class="rule-blue-thin"></div>
</main>
</body>
</html>
```